Postcard Design

Cinder Vale Partners is a waste and Recycling company. We want to purchase recyclable materials from businesses. We would like to use the colors green and grey. The exact colors needed in this project are described below. We would like to have a picture of waste cardboard,a picture of money, and and the line- Are you getting top dollar for your Recyclables? After please put our logo and our phone number: 800.742.5196, our website (bronlomar.com),
and our email address: marisol@bronlomar.com.

* Postcard must contain our logo. Please see buisness card for branding

Industry/Entity Type

It Company

Requirements
Must have
• This postcard must contain the logo and these colors:
Pantone: 576C & 418C

```html
<!DOCTYPE html>
<html lang="en">
<head>
<meta charset="utf-8">
<title>Cinder Vale Partners Postcard</title>
<link href="https://fonts.googleapis.com/css2?family=Roboto+Condensed:wght@400;700&family=Archivo:wght@700;800&display=swap" rel="stylesheet">
<style>
  :root {
    --backdrop: #8a8b8f;
    --card: #ffffff;
    --green: #5a8a35;
    --grey-text: #6d6c5f;
    --olive-bar: #5f5e4f;
    --chevron-yellow: #f2e417;
    --band-grey: #e4e5e3;
  }
  * { margin: 0; padding: 0; box-sizing: border-box; }
  html, body { width: 1200px; height: 959px; overflow: hidden; }
  body { background: var(--backdrop); position: relative; }
  .postcard {
    position: absolute; left: 76px; top: 76px; width: 1046px; height: 805px;
    background: var(--card); overflow: hidden;
  }
  .photo { position: absolute; }
  .photo-cardboard {
    left: 64px; top: 120px; width: 416px; height: 275px;
    background: linear-gradient(180deg, #d6b98c 0%, #c7a475 55%, #b38f61 100%);
    border-radius: 4px;
  }
  .photo-money {
    left: 566px; top: 36px; width: 410px; height: 385px;
    background: radial-gradient(ellipse at 50% 30%, #cfd6c2 0%, #b9a98a 55%, #a88d66 100%);
    border-radius: 40% 40% 30% 30%;
  }
  .flow-arrow { position: absolute; left: 489px; top: 207px; }
  .headline-band {
    position: absolute; left: 0; top: 480px; width: 100%; height: 104px;
    background: linear-gradient(180deg, #ffffff 0%, var(--band-grey) 100%);
  }
  .headline {
    position: absolute; left: 78px; top: 448px;
    font-family: "Archivo", Arial, sans-serif; font-weight: 800;
    font-size: 43px; line-height: 56px; color: var(--grey-text);
    letter-spacing: 0.5px;
  }
  .headline .accent { color: var(--green); }
  .contact-label {
    position: absolute; left: 86px; top: 643px;
    font-family: "Roboto Condensed", Arial, sans-serif; font-size: 19px; color: #222;
  }
  .contact-name {
    position: absolute; left: 84px; top: 677px;
    font-family: "Roboto Condensed", Arial, sans-serif; font-weight: 700;
    font-size: 29px; color: var(--green); letter-spacing: 0.3px;
  }
  .brand {
    position: absolute; left: 722px; top: 668px;
    display: flex; align-items: center; gap: 12px;
  }
  .brand-square { width: 26px; height: 26px; background: var(--green); }
  .brand-name {
    font-family: "Roboto Condensed", Arial, sans-serif; font-weight: 700;
    font-size: 32px; color: var(--grey-text);
  }
  .contact-bar {
    position: absolute; left: 0; top: 752px; width: 100%; height: 53px;
    background: var(--olive-bar);
    display: flex; align-items: center; padding-left: 92px; gap: 20px;
    font-family: "Roboto Condensed", Arial, sans-serif; font-weight: 700;
    font-size: 27px; color: #fff;
  }
  .contact-item { display: flex; align-items: center; gap: 8px; }
</style>
</head>
<body>
  <main class="postcard">
    <div class="photo photo-cardboard" role="img" aria-label="Stack of flattened waste cardboard tied with string"></div>

    <svg class="flow-arrow" width="72" height="58" viewBox="0 0 72 58" aria-hidden="true">
      <polygon points="0,0 18,0 40,29 18,58 0,58 22,29" fill="var(--green)"/>
      <polygon points="30,0 48,0 70,29 48,58 30,58 52,29" fill="var(--green)"/>
    </svg>

    <div class="photo photo-money" role="img" aria-label="Burlap sack overflowing with hundred dollar bills"></div>

    <div class="headline-band"></div>
    <h1 class="headline">
      ARE YOU GETTING <span class="accent">TOP DOLLAR</span><br>
      FOR YOUR <span class="accent">RECYCLABLES?</span>
    </h1>

    <p class="contact-label">For More Info Contact :</p>
    <p class="contact-name">MARISOL DELCOURT</p>

    <div class="brand">
      <span class="brand-square"></span>
      <span class="brand-name">Cinder Vale Partners</span>
    </div>

    <footer class="contact-bar">
      <span class="contact-item">
        <svg width="26" height="20" viewBox="0 0 26 20" aria-hidden="true"><polygon points="0,0 7,0 13,10 7,20 0,20 6,10" fill="var(--chevron-yellow)"/><polygon points="12,0 19,0 25,10 19,20 12,20 18,10" fill="var(--chevron-yellow)"/></svg>
        800.742.5196
      </span>
      <span class="contact-item">
        <svg width="26" height="20" viewBox="0 0 26 20" aria-hidden="true"><polygon points="0,0 7,0 13,10 7,20 0,20 6,10" fill="var(--chevron-yellow)"/><polygon points="12,0 19,0 25,10 19,20 12,20 18,10" fill="var(--chevron-yellow)"/></svg>
        marisol@bronlomar.com.
      </span>
      <span class="contact-item">
        <svg width="26" height="20" viewBox="0 0 26 20" aria-hidden="true"><polygon points="0,0 7,0 13,10 7,20 0,20 6,10" fill="var(--chevron-yellow)"/><polygon points="12,0 19,0 25,10 19,20 12,20 18,10" fill="var(--chevron-yellow)"/></svg>
        www.bronlomar.com
      </span>
    </footer>
  </main>
</body>
</html>
```